Business card for a restaurant/bar

We are looking for a business card design/template for TANKO Riverside that can be a starting point for a corporate identity pack. We are known for live bands on the weekends, sports, burgers, beers and American cuisine. We have a relaxing/friendly environment and our tag line is "No 'tudes. Just sports, great food, great music and great times." We are located down the street from a college campus and we attract a wide variety of customers from college students, business professionals, and those interested in sports and general trivia.
Visit our website: www.tankoriverside-example.com and see the attached files for more info about us.
Please use the current logo.

```html
<!DOCTYPE html>
<html lang="en">
<head>
<meta charset="utf-8">
<title>TANKO Riverside – Business Card</title>
<link href="https://fonts.googleapis.com/css2?family=Oswald:wght@600&family=Courier+Prime&family=Cabin+Sketch:wght@400;700&family=Architects+Daughter&display=swap" rel="stylesheet">
<style>
  :root {
    --page-bg: #b3b3b4;
    --teal: #0c4a4f;
    --charcoal: #2c2c2e;
    --plate-dark: #1d1d1f;
    --plate-metal: #4a4a4c;
    --back-teal: #03292a;
    --paper: #ffffff;
    --ink: #1a1a1a;
    --chalk: #d9dcdc;
    --dash: #e6e6e6;
    --accent-red: #b3121a;
  }
  * { margin: 0; padding: 0; box-sizing: border-box; }
  html, body { width: 1200px; height: 1094px; overflow: hidden; background: var(--page-bg); }
  .canvas { position: relative; width: 1200px; height: 1094px; }

  .card { position: absolute; top: 28px; width: 544px; height: 914px; overflow: hidden; }
  .card--front { left: 39px; background: var(--charcoal); }
  .card--back { left: 608px; background: var(--back-teal); }

  .band { position: absolute; left: 0; width: 100%; }
  .dash { position: absolute; left: 0; width: 100%; border-top: 2px dashed var(--dash); }

  .headline {
    font-family: "Oswald", sans-serif; font-weight: 600; color: #fff;
    text-align: center; letter-spacing: 3px; white-space: nowrap;
  }

  /* front */
  .front-top { top: 0; height: 88px; background: var(--teal); }
  .front-top .headline { font-size: 56px; line-height: 88px; }
  .logo-area { top: 88px; height: 318px; background: var(--charcoal); }
  .logo-plate {
    position: absolute; left: 7px; top: 17px; width: 527px; height: 285px;
    background: var(--plate-dark); display: flex; align-items: center; justify-content: center;
  }
  .logo-plate__inner {
    width: 493px; height: 251px; border: 3px solid var(--accent-red);
    display: flex; align-items: center; justify-content: center; gap: 18px;
    background: var(--plate-metal);
  }
  .logo-mark { width: 30px; height: 30px; background: var(--accent-red); flex: none; }
  .logo-name {
    font-family: "Oswald", sans-serif; font-weight: 600; font-size: 54px;
    color: #ffffff; letter-spacing: 2px; white-space: nowrap;
  }
  .seat-band { top: 406px; height: 55px; background: var(--teal);
    font-family: "Courier Prime", monospace; font-size: 25px; color: #fff; line-height: 55px; }
  .seat-band span { position: absolute; top: 0; }
  .tagline {
    top: 461px; height: 164px; background: var(--charcoal);
    font-family: "Courier Prime", monospace; font-size: 29px; line-height: 38px; color: #fff;
    padding-top: 24px; white-space: nowrap;
  }
  .tagline span { display: block; }
  .contact { top: 625px; height: 201px; background: var(--paper);
    font-family: "Courier Prime", monospace; color: var(--ink); }
  .contact .addr { position: absolute; left: 20px; top: 14px; font-size: 27px; line-height: 34px; white-space: nowrap; }
  .contact .addr .city { display: block; padding-left: 250px; }
  .contact .phone { position: absolute; left: 20px; top: 96px; font-size: 28px; line-height: 34px; letter-spacing: 1px; }
  .contact .web { position: absolute; left: 20px; top: 157px; font-size: 26px; line-height: 34px; white-space: nowrap; }
  .front-bottom { top: 826px; height: 88px; background: var(--teal); }
  .front-bottom .headline { font-size: 56px; line-height: 88px; }

  /* back */
  .back-head { top: 0; height: 91px; }
  .back-head .headline, .back-foot .headline { color: var(--chalk); }
  .back-head .headline { font-size: 56px; line-height: 88px; }
  .checklist { position: absolute; left: 45px; top: 119px; list-style: none;
    font-family: "Cabin Sketch", sans-serif; font-size: 40px; color: var(--chalk); }
  .checklist li { display: flex; align-items: center; height: 66px; }
  .checklist span { width: 160px; }
  .checklist svg { width: 68px; height: 54px; }
  .illustration {
    position: absolute; left: 295px; top: 114px; width: 224px; height: 265px;
    background: radial-gradient(circle at 55% 55%, #2a4a4a 0%, #0c3434 55%, var(--back-teal) 100%);
    border-radius: 12px;
  }
  .back-logo { position: absolute; top: 463px; left: 0; width: 100%; height: 362px;
    display: flex; align-items: center; justify-content: center; }
  .back-logo .logo-name { color: var(--chalk); font-size: 60px; }
  .back-foot { top: 825px; height: 89px; }
  .back-foot .headline { font-size: 50px; line-height: 89px; }

  .side-label { position: absolute; top: 962px; font-family: "Architects Daughter", cursive;
    font-size: 54px; line-height: 80px; color: #111; letter-spacing: 2px; }
</style>
</head>
<body>
<main class="canvas">
  <section class="card card--front" aria-label="Card front">
    <div class="band front-top"><h1 class="headline">FIELD LEVEL</h1></div>
    <div class="dash" style="top:88px"></div>
    <div class="band logo-area">
      <div class="logo-plate"><div class="logo-plate__inner">
        <span class="logo-mark"></span><span class="logo-name">TANKO Riverside</span>
      </div></div>
    </div>
    <div class="dash" style="top:406px"></div>
    <div class="band seat-band">
      <span style="left:62px">SEC</span><span style="left:232px">ROW</span><span style="left:386px">SEAT</span>
    </div>
    <p class="band tagline">
      <span style="margin-left:30px">"No 'tudes. Just sports,</span>
      <span style="margin-left:49px">great food, great music</span>
      <span style="margin-left:170px">and great times."</span>
    </p>
    <div class="band contact">
      <p class="addr">418 West Campus Row Ave.<span class="city">Riverside,CA</span></p>
      <p class="phone">(555) 014-2387</p>
      <div class="dash" style="top:146px; border-color:#222"></div>
      <p class="web">www.tankoriverside-example.com</p>
    </div>
    <div class="band front-bottom"><p class="headline">ADMIT ALL</p></div>
  </section>

  <section class="card card--back" aria-label="Card back">
    <div class="band back-head"><h2 class="headline">TEAM TANKO</h2></div>
    <div class="dash" style="top:91px"></div>
    <ul class="checklist">
      <li><span>SPORTS</span><svg viewBox="0 0 72 56"><circle cx="22" cy="32" r="16" fill="none" stroke="#d9dcdc" stroke-width="4"/><path d="M12 30 L22 42 L66 6" fill="none" stroke="#d9dcdc" stroke-width="5" stroke-linecap="round"/></svg></li>
      <li><span>MUSIC</span><svg viewBox="0 0 72 56"><circle cx="22" cy="32" r="16" fill="none" stroke="#d9dcdc" stroke-width="4"/><path d="M12 30 L22 42 L66 6" fill="none" stroke="#d9dcdc" stroke-width="5" stroke-linecap="round"/></svg></li>
      <li><span>FOOD</span><svg viewBox="0 0 72 56"><circle cx="22" cy="32" r="16" fill="none" stroke="#d9dcdc" stroke-width="4"/><path d="M12 30 L22 42 L66 6" fill="none" stroke="#d9dcdc" stroke-width="5" stroke-linecap="round"/></svg></li>
      <li><span>FUN</span><svg viewBox="0 0 72 56"><circle cx="22" cy="32" r="16" fill="none" stroke="#d9dcdc" stroke-width="4"/><path d="M12 30 L22 42 L66 6" fill="none" stroke="#d9dcdc" stroke-width="5" stroke-linecap="round"/></svg></li>
    </ul>
    <div class="illustration" role="img" aria-label="Chalk drawing of a beer mug, a burger and music notes"></div>
    <div class="dash" style="top:406px"></div>
    <div class="dash" style="top:461px"></div>
    <div class="back-logo"><span class="logo-name">TANKO Riverside</span></div>
    <div class="dash" style="top:825px"></div>
    <div class="band back-foot"><p class="headline">AWESOME</p></div>
  </section>

  <p class="side-label" style="left:184px">FRONT</p>
  <p class="side-label" style="left:793px">BACK</p>
</main>
</body>
</html>
```